Meridell Wellness Website Meridell Herbal Restorative Products/Services, Ecommerce, Appt Book

We at MeridellWellness.example need a clean website home and interior pages designed for our luxury all-natural and prescription drug-FREE brand, Meridell Herbal Restoratives.

Meridell Herbal Restoratives
Aligned With Nature
Est. Aspen, Colorado

We deliver phytoncide and plant medicines as well as essential oils, vitamins, supplements, minerals, herbs, other skin, cosmetic, beauty products, products for the home and office, pet products and health products along with the following services :
nutrition counseling
nutrient therapy
herbalism
herbalism formulas

What differentiates Meridell Wellness is our exclusive
forest therapy
nature therapy
ski therapy
white water rafting therapy
golf therapy
equine therapy
and other high end recreational therapy solutions in Aspen and Vail Colorado.

We also offer luxury nature themed retreats and glamping (glamourous luxury camping) retreats in Aspen, Vail, California and Hawaii

And deliver all-natural plant based therapeutic treatments to heal, reverse or prevent mental illness and drug or alcohol addictions

We are HQ in Aspen Colorado with locations in Vail, California, Hawaii ...

The store and products is a subsidiary of CorvantClinicians.example

We heal, reverse and prevent chronic illness and disease naturally without pharmaceutical drugs of any kind. Our main firm is a concierge medical firm which offers concierge medical services to high net worth clients, executives, families, kids and corporations.

Colors to use :

White (lots of white space, clean, luxury, pure, healing)
Green (paying homage to our therapeutic remedies trees, plants, forests)
Shiny Silver/Platinum/Chrome (think Halden Voss logo)

Here are the main links for the website :

Meridell Wellness Store

Nutrition & Nutrient Therapy
Herbal Apothecary
Vitamins, Minerals and Supplements
Forest, Ski, Surf , Golf, Equine Therapy
Luxury Health Retreats
Glamping Health Camps
Contact
About
Blog

Home page and interior pages design
Will have a ecommerce to purchase the products direct
Will have an appointment booking section for recreational therapy or nutrition or herbalism consults
Will have an online consultation booking section
Will have a retreat/vacation/camp reservation page

Target Market(s)

Luxury and high net-worth or wealthy health conscious consumers, natural health consumers, concierge consumers, Nutrition and outdoor recreation consumers , Aspen and Vail travelers, skiers, golfers, hikers, white water rafting enthusiasts, executives/ceo's and retirees as well as those individuals including kids interested in nature, hiking, ski, camping luxury camps (glamping) ... All services are all concierge level and we cater those who need natural sustainable cures for everything from mental health, senior health, impotence, weight loss/weight management, fatigue/low energy, hormonal balance for men and women etc.

Coding

Coded - Design and coding required

Number of Pages Required

5+ page

Requirements
Must have
• Use same consistent font and colors as the brand. See attachments.
• Must have a main gallery on the home page where we will cycle thru images of our products, images of the forests, wildlife and video experiences ...
• Please use consistent fonts and the colors should be white, green (plants/trees/especially forests) and platinum/shiny chrome/silver)
• Trees from the aspen forests b/c all of our products are created from nature, plants and phytoncides. Phytoncides are substances emitted from plants and trees. These substances have natural healing powers to eliminate stress, kill cancer cells, lower blood pressure, improve immune functioning, etc.
• You can get a great visual checking out the images (and take what you need for the main gallery on the site) at our twitter feed, see images @meridellwellness
• We will later request that you do markup of psd files to htiml
• This site will be most likely done in wordpress
Nice to have
• We also offer online consultations so it would be good to add some type of video link or chat feature, a sneak peak of our twitter feed from @meridellwellness and the footer can look similar to the one we have a corvantclinicians.example
Should not have
• No other colors outside of our current branding choices

```html
<!DOCTYPE html>
<html lang="en">
<head>
<meta charset="utf-8">
<title>Meridell Wellness — Home</title>
<link href="https://fonts.googleapis.com/css2?family=Open+Sans:ital,wght@0,400;0,600;0,700;1,400&family=Roboto:wght@400;500;700&family=Roboto+Condensed:wght@700&display=swap" rel="stylesheet">
<style>
:root{
  --green:#8cc63e;
  --green-dark:#74ad2b;
  --ink:#333333;
  --muted:#6f6f6f;
  --line:#e2e2e2;
  --charcoal:#2f2f2f;
  --footer:#333333;
  --footer-bottom:#222222;
  --white:#ffffff;
  --nav-active:#3b3b3b;
}
*{box-sizing:border-box;margin:0;padding:0}
html,body{width:1200px;height:3564px;overflow:hidden}
body{font-family:"Open Sans",Arial,sans-serif;color:var(--ink);background:var(--white);position:relative}
.wrap{width:1006px;margin:0 auto;position:relative}
section,header,nav,footer{position:relative;width:1200px}

/* header */
.topbar{height:130px}
.topbar .phone{position:absolute;left:97px;top:46px;display:flex;align-items:center;gap:14px}
.phone .dot{width:34px;height:34px;border-radius:50%;background:var(--green);display:flex;align-items:center;justify-content:center}
.phone p{font-family:"Roboto",Arial,sans-serif;font-size:14px;line-height:17px;color:var(--ink)}
.brand{position:absolute;left:430px;top:44px;width:340px;display:flex;align-items:center;justify-content:center;gap:12px;font-family:"Roboto",Arial,sans-serif;font-weight:500;font-size:12px;letter-spacing:.5px;color:var(--ink);text-transform:uppercase}
.brand .mark{width:40px;height:40px;background:var(--charcoal)}
.search{position:absolute;right:100px;top:50px;width:232px;height:34px;border:1px solid #cfcfcf;display:flex;align-items:center;justify-content:space-between;padding:0 10px;font-family:"Roboto",Arial,sans-serif;font-size:12px;color:var(--ink)}

.mainnav{height:53px;background:var(--green)}
.mainnav ul{list-style:none;display:flex;position:absolute;left:97px;top:0;height:53px}
.mainnav li{font-family:"Roboto",Arial,sans-serif;font-size:13px;color:var(--white);text-transform:uppercase;height:53px;line-height:53px;padding:0 20px;letter-spacing:.3px}
.mainnav li.active{background:var(--nav-active)}
.mainnav li:last-child{padding-right:0}

/* hero */
.hero{height:513px;background:linear-gradient(100deg,#d9c3a6 0%,#c99772 22%,#e7ddc4 42%,#b9b35a 62%,#8d9a3a 82%,#c3a44a 100%)}
.hero .photo{position:absolute;inset:0}
.hero h1{position:absolute;right:98px;top:200px;text-align:right;font-family:"Roboto Condensed",Arial,sans-serif;font-weight:700;font-size:30px;line-height:41px;color:var(--white);text-transform:uppercase;letter-spacing:.3px}
.hero .arrow{position:absolute;top:256px;width:34px;height:34px;border-radius:50%;background:rgba(0,0,0,.3)}
.hero .arrow.prev{left:46px}.hero .arrow.next{right:46px}
.hero .arrow svg{position:absolute;left:11px;top:10px}

.section-title{font-family:"Roboto",Arial,sans-serif;font-weight:400;font-size:32px;text-align:center;text-transform:uppercase;color:var(--ink)}

/* services */
.services{height:425px}
.services .section-title{padding-top:53px}
.service-list{display:flex;justify-content:space-between;position:absolute;left:97px;top:146px;width:1006px}
.service{width:240px;text-align:center}
.service .icon{width:104px;height:104px;border-radius:50%;background:var(--green);margin:0 auto;border:4px solid #e6f2d6;display:flex;align-items:center;justify-content:center}
.service h3{font-family:"Roboto",Arial,sans-serif;font-weight:400;font-size:14px;margin-top:24px;text-transform:uppercase;color:var(--ink)}
.service p{font-size:11px;line-height:17px;color:var(--muted);margin-top:10px;padding:0 6px}

/* differentiators */
.exclusive{height:542px;background:var(--green)}
.exclusive h2{font-family:"Roboto Condensed",Arial,sans-serif;font-weight:700;font-size:28px;color:var(--white);text-align:center;text-transform:uppercase;padding-top:68px}
.cards{position:absolute;left:97px;top:148px;width:1006px;display:flex;justify-content:space-between}
.card{width:240px;height:290px;background:var(--white)}
.card .img{height:170px}
.card h3{font-family:"Open Sans",Arial,sans-serif;font-weight:400;font-size:19px;text-align:center;margin-top:14px;color:var(--ink)}
.card p{font-size:11px;line-height:16px;color:var(--muted);text-align:center;margin-top:8px;padding:0 18px}
.dots{position:absolute;top:486px;left:0;width:1200px;display:flex;justify-content:center;gap:6px}
.dots span{width:12px;height:12px;border-radius:50%;border:2px solid var(--white)}
.dots span.on{background:var(--white)}

/* products */
.products{height:527px}
.products .section-title{padding-top:50px}
.leaf{position:absolute;top:0;width:90px;height:170px;background:radial-gradient(ellipse at center,#7fbf2f 0%,#9bd14f 55%,rgba(255,255,255,0) 72%)}
.leaf.left{left:-20px}.leaf.right{right:-20px}
.product-list{position:absolute;left:97px;top:143px;width:1006px;display:flex;justify-content:space-between}
.product{width:240px;text-align:center}
.product .img{width:140px;height:190px;margin:0 auto;background:linear-gradient(180deg,#fbfbfb,#e4e4e4)}
.product h3{font-family:"Open Sans",Arial,sans-serif;font-weight:400;font-size:19px;color:var(--green);margin-top:24px}
.product p{font-size:11px;line-height:16px;color:var(--muted);margin-top:4px;padding:0 14px}
.product .buy{display:flex;align-items:center;justify-content:space-between;padding:0 6px;margin-top:20px}
.product .price{font-family:"Roboto",Arial,sans-serif;font-size:20px;color:var(--ink)}
.product .cart{border:2px solid var(--green);border-radius:16px;font-size:10px;color:var(--green);padding:5px 14px;text-transform:uppercase}

/* appointment */
.booking{height:395px;background:linear-gradient(90deg,#2c2c2c 0%,#3d3a33 45%,#2f3a24 100%)}
.booking .photo{position:absolute;inset:0}
.booking h2{position:relative;font-family:"Roboto",Arial,sans-serif;font-weight:500;font-size:36px;color:var(--white);text-align:center;text-transform:uppercase;padding-top:88px}
.booking form{position:absolute;left:173px;top:176px;width:842px;display:grid;grid-template-columns:276px 276px 276px;column-gap:7px;row-gap:11px}
.field{height:46px;background:var(--white);font-size:11px;font-style:italic;color:#555;padding:0 14px;line-height:46px}
.field.submit{background:var(--green);color:var(--white);font-style:normal;font-weight:700;text-transform:uppercase;text-align:center;font-size:12px}

/* blog */
.blog{height:532px}
.blog .section-title{padding-top:56px}
.posts{position:absolute;left:97px;top:124px;width:1006px;display:flex;justify-content:space-between}
.post{width:312px}
.post .img{height:190px;position:relative}
.post .date{position:absolute;left:14px;top:0;width:66px;height:72px;background:var(--green);color:var(--white);text-align:center;font-family:"Roboto",Arial,sans-serif}
.post .date small{display:block;font-size:9px;text-transform:uppercase;padding-top:8px}
.post .date b{display:block;font-size:24px;line-height:26px}
.post .date i{display:block;font-style:normal;font-size:11px}
.post h3{font-family:"Open Sans",Arial,sans-serif;font-weight:400;font-size:15px;margin-top:22px;color:var(--ink)}
.post .meta{display:flex;align-items:center;gap:20px;margin-top:12px;font-size:11px;color:var(--muted)}
.stars{color:#f2b01e;font-size:11px;letter-spacing:1px}
.stars em{color:#ccc;font-style:normal}
.post p{font-size:11px;line-height:16px;color:var(--muted);margin-top:12px}

/* subscribe */
.subscribe{height:102px;background:var(--green)}
.subscribe .envelope{position:absolute;left:84px;top:12px;width:90px;height:76px;opacity:.35}
.subscribe .plane{position:absolute;left:188px;top:34px}
.subscribe p{position:absolute;left:244px;top:30px;font-family:"Roboto",Arial,sans-serif;font-size:14px;line-height:19px;color:var(--white);text-transform:uppercase;font-weight:500}
.subscribe .email{position:absolute;left:560px;top:31px;width:500px;height:40px;border-radius:20px;background:var(--white);overflow:hidden}
.subscribe .email span{position:absolute;left:22px;top:12px;font-size:12px;color:#777}
.subscribe .email b{position:absolute;right:0;top:0;width:128px;height:40px;background:var(--charcoal);color:var(--white);font-family:"Roboto",Arial,sans-serif;font-weight:500;font-size:12px;text-transform:uppercase;line-height:40px;text-align:center}

/* footer */
.site-footer{height:293px;background:var(--footer);color:var(--white)}
.site-footer h4{font-family:"Roboto",Arial,sans-serif;font-weight:500;font-size:16px;text-transform:uppercase;color:var(--white)}
.fcol{position:absolute;top:52px}
.fcol.contact{left:97px;width:260px}
.fcol.store{left:394px}
.fcol.branches{left:702px}
.fcol.consult{left:874px;top:50px;width:230px}
.contact .row{display:flex;gap:20px;align-items:flex-start;font-size:12px;line-height:17px;margin-top:18px}
.contact .row:first-of-type{margin-top:26px}
.contact .row svg{flex:none}
.social{display:flex;gap:6px;margin-top:22px}
.social span{width:22px;height:22px;border-radius:50%;border:1px solid #bdbdbd}
.site-footer ul{list-style:none;margin-top:22px}
.site-footer li{font-size:12px;line-height:25px;color:#e8e8e8}
.consult .in{height:42px;background:var(--white);margin-top:12px;font-size:11px;color:#444;padding:0 12px;line-height:42px;position:relative}
.consult .in:first-of-type{margin-top:22px}
.consult .in b{position:absolute;right:8px;top:7px;height:28px;line-height:28px;padding:0 14px;background:var(--green);color:var(--white);font-weight:600;font-size:11px;text-transform:uppercase}
.bottom{height:52px;background:var(--footer-bottom);color:#dcdcdc;font-size:11px;text-align:center;line-height:52px}
</style>
</head>
<body>

<header class="topbar">
  <div class="phone">
    <div class="dot"><svg width="16" height="16" viewBox="0 0 24 24"><path fill="#fff" d="M6.6 10.8a15.1 15.1 0 0 0 6.6 6.6l2.2-2.2c.3-.3.7-.4 1-.2 1.1.4 2.3.6 3.6.6.6 0 1 .4 1 1V20c0 .6-.4 1-1 1A17 17 0 0 1 3 4c0-.6.4-1 1-1h3.5c.6 0 1 .4 1 1 0 1.3.2 2.5.6 3.6.1.3 0 .7-.2 1z"/></svg></div>
    <p>84-4 MERIDELL<br>(1-844-555-0137)</p>
  </div>
  <div class="brand"><span>Corvant Clinicians</span><span class="mark"></span><span>Corvant Partners</span></div>
  <div class="search"><span>SEARCH</span><svg width="13" height="13" viewBox="0 0 24 24"><circle cx="10" cy="10" r="7" fill="none" stroke="#333" stroke-width="3"/><path d="M15 15l6 6" stroke="#333" stroke-width="3"/></svg></div>
</header>

<nav class="mainnav">
  <ul>
    <li class="active">Home</li><li>About</li><li>Services</li><li>Client-in-Chief Care</li><li>Events</li><li>Support Group</li><li>Store</li><li>Blog</li><li>Contact</li>
  </ul>
</nav>

<section class="hero">
  <div class="photo" role="img" aria-label="Slideshow photo of a relaxed woman outdoors among sunlit green foliage"></div>
  <span class="arrow prev"><svg width="12" height="14" viewBox="0 0 12 14"><path d="M8 2L3 7l5 5" fill="none" stroke="#fff" stroke-width="2"/></svg></span>
  <span class="arrow next"><svg width="12" height="14" viewBox="0 0 12 14"><path d="M4 2l5 5-5 5" fill="none" stroke="#fff" stroke-width="2"/></svg></span>
  <h1>Meridell Herbal<br>Restoratives Aligned With<br>Nature Est. Aspen, Colorado</h1>
</section>

<section class="services">
  <h2 class="section-title">Our Services</h2>
  <div class="service-list">
    <div class="service"><div class="icon"><svg width="44" height="44" viewBox="0 0 44 44"><rect x="9" y="6" width="26" height="32" rx="3" fill="#fff"/><path d="M15 16h14M15 22h14M15 28h9" stroke="#8cc63e" stroke-width="2.5"/></svg></div><h3>Nutrition Counseling</h3><p>Neque porro quisquam est, qui dolorem ipsum quia dolor sit amet, consectetur, adipisci velit, sed quia non</p></div>
    <div class="service"><div class="icon"><svg width="44" height="44" viewBox="0 0 44 44"><rect x="14" y="8" width="16" height="6" rx="2" fill="#fff"/><rect x="10" y="16" width="24" height="22" rx="4" fill="#fff"/><path d="M22 21v12M16 27h12" stroke="#8cc63e" stroke-width="3"/></svg></div><h3>Nutrient Therapy</h3><p>Neque porro quisquam est, qui dolorem ipsum quia dolor sit amet, consectetur, adipisci velit, sed quia non</p></div>
    <div class="service"><div class="icon"><svg width="44" height="44" viewBox="0 0 44 44"><path d="M7 20h30a15 15 0 0 1-30 0z" fill="#fff"/><path d="M26 18L34 6" stroke="#fff" stroke-width="4" stroke-linecap="round"/><rect x="15" y="34" width="14" height="4" fill="#fff"/></svg></div><h3>Herbalism</h3><p>Neque porro quisquam est, qui dolorem ipsum quia dolor sit amet, consectetur, adipisci velit, sed quia non</p></div>
    <div class="service"><div class="icon"><svg width="44" height="44" viewBox="0 0 44 44"><path d="M36 8C16 8 8 18 10 34 26 34 36 24 36 8z" fill="#fff"/><path d="M8 38L28 16" stroke="#8cc63e" stroke-width="2.5"/></svg></div><h3>Herbalism Formulas</h3><p>Neque porro quisquam est, qui dolorem ipsum quia dolor sit amet, consectetur, adipisci velit, sed quia non</p></div>
  </div>
</section>

<section class="exclusive">
  <h2>What differentiates Meridell Wellness is our exclusive</h2>
  <div class="cards">
    <div class="card"><div class="img" role="img" aria-label="Photo of stacked stones beside a forest stream" style="background:linear-gradient(180deg,#8c9188,#5d625a 60,#9aa39c)"></div><h3>Forest Therapy</h3><p>Mauris vel lacus vitae felis vestibulum volutpat imperdiet ac nisl Cum sociis natoque sodales velit</p></div>
    <div class="card"><div class="img" role="img" aria-label="Photo of a spa treatment with candles and green leaves" style="background:linear-gradient(180deg,#6aa22e,#c8b79a 55%,#4e3a22)"></div><h3>Nature Therapy</h3><p>Mauris vel lacus vitae felis vestibulum volutpat imperdiet ac nisl Cum sociis natoque sodales velit</p></div>
    <div class="card"><div class="img" role="img" aria-label="Photo of a facial skin treatment at a spa" style="background:linear-gradient(180deg,#a07a60,#e2c3ac 50%,#d8d1c8)"></div><h3>Ski Therapy</h3><p>Mauris vel lacus vitae felis vestibulum volutpat imperdiet ac nisl Cum sociis natoque sodales velit</p></div>
    <div class="card"><div class="img" role="img" aria-label="Photo of a golf instructor with a player on a sunny course" style="background:linear-gradient(180deg,#9fc3df,#7fae3e 60%,#5f8e2a)"></div><h3>Golf Therapy</h3><p>Mauris vel lacus vitae felis vestibulum volutpat imperdiet ac nisl Cum sociis natoque sodales velit</p></div>
  </div>
  <div class="dots"><span class="on"></span><span></span><span></span><span></span></div>
</section>

<section class="products">
  <div class="leaf left" role="img" aria-label="Green leaf decoration"></div>
  <div class="leaf right" role="img" aria-label="Green leaf decoration"></div>
  <h2 class="section-title">Our Products</h2>
  <div class="product-list">
    <div class="product"><div class="img" role="img" aria-label="Product photo of a white supplement bottle"></div><h3>Product Name</h3><p>Ut nisi erat fermentum vel congue id euismod in elit Fusce</p><div class="buy"><span class="price">$25.99</span><span class="cart">Add to cart</span></div></div>
    <div class="product"><div class="img" role="img" aria-label="Product photo of a cream tube with green cap" style="background:linear-gradient(180deg,#f3f3ea 70%,#8cc63e)"></div><h3>Product Name</h3><p>Ut nisi erat fermentum vel congue id euismod in elit Fusce</p><div class="buy"><span class="price">$25.99</span><span class="cart">Add to cart</span></div></div>
    <div class="product"><div class="img" role="img" aria-label="Product photo of an essential oil dropper bottle" style="background:linear-gradient(180deg,#e8e8e8,#bdbdbd 55%,#2a2a2a)"></div><h3>Product Name</h3><p>Ut nisi erat fermentum vel congue id euismod in elit Fusce</p><div class="buy"><span class="price">$25.99</span><span class="cart">Add to cart</span></div></div>
    <div class="product"><div class="img" role="img" aria-label="Product photo of a herbal tea pouch with leaves" style="background:linear-gradient(180deg,#f2f2ec,#a9b89a)"></div><h3>Product Name</h3><p>Ut nisi erat fermentum vel congue id euismod in elit Fusce</p><div class="buy"><span class="price">$25.99</span><span class="cart">Add to cart</span></div></div>
  </div>
</section>

<section class="booking">
  <div class="photo" role="img" aria-label="Dark background photo of a relaxed spa guest and green leaves"></div>
  <h2>Appointment Booking</h2>
  <form>
    <div class="field">Your first name</div><div class="field">Your last name</div><div class="field">Your email</div>
    <div class="field">Your mobile</div><div class="field">Leave a Comment</div><div class="field submit">Appointment Booking</div>
  </form>
</section>

<section class="blog">
  <h2 class="section-title">Recent Blog Articles</h2>
  <div class="posts">
    <div class="post"><div class="img" role="img" aria-label="Photo of a relaxing massage treatment" style="background:linear-gradient(180deg,#c98a55,#e6c2a0 60%,#efe7dd)"><div class="date"><small>April</small><b>02</b><i>2016</i></div></div><h3>Meridell Herbal Restoratives</h3><div class="meta"><span class="stars">★★★<em>★★</em></span><span>No comments</span></div><p>Neque porro quisquam est, qui dolorem ipsum quia dolor sit amet, consectetur, adipisci velit, sed quia non numquam eius modi tempora incidunt ut labore et</p></div>
    <div class="post"><div class="img" role="img" aria-label="Photo of two women talking on a sofa" style="background:linear-gradient(180deg,#b4a58c,#6b4c36 55%,#3a2b22)"><div class="date"><small>April</small><b>02</b><i>2016</i></div></div><h3>Meridell Herbal Restoratives</h3><div class="meta"><span class="stars">★★★<em>★★</em></span><span>No comments</span></div><p>Neque porro quisquam est, qui dolorem ipsum quia dolor sit amet, consectetur, adipisci velit, sed quia non numquam eius modi tempora incidunt ut labore et</p></div>
    <div class="post"><div class="img" role="img" aria-label="Photo of two runners jogging on a country road" style="background:linear-gradient(180deg,#d7e3ea,#8aa56a 55%,#6f6f6f)"><div class="date"><small>April</small><b>02</b><i>2016</i></div></div><h3>Meridell Herbal Restoratives</h3><div class="meta"><span class="stars">★★★<em>★★</em></span><span>No comments</span></div><p>Neque porro quisquam est, qui dolorem ipsum quia dolor sit amet, consectetur, adipisci velit, sed quia non numquam eius modi tempora incidunt ut labore et</p></div>
  </div>
</section>

<section class="subscribe">
  <svg class="envelope" viewBox="0 0 90 76"><g transform="rotate(-15 45 38)"><rect x="8" y="16" width="74" height="46" fill="none" stroke="#fff" stroke-width="3"/><path d="M8 16l37 26 37-26" fill="none" stroke="#fff" stroke-width="3"/></g></svg>
  <svg class="plane" width="40" height="34" viewBox="0 0 40 34"><path d="M2 16L38 2 30 32 18 22z" fill="none" stroke="#fff" stroke-width="2.5" stroke-linejoin="round"/><path d="M18 22L38 2" stroke="#fff" stroke-width="2.5"/></svg>
  <p>Subscribe to receive updates and<br>exclusive offers.</p>
  <div class="email"><span>Enter your E - mail</span><b>Subscribe</b></div>
</section>

<footer class="site-footer">
  <div class="fcol contact">
    <h4>Contact Us</h4>
    <div class="row"><svg width="16" height="20" viewBox="0 0 16 20"><path d="M8 1a6 6 0 0 0-6 6c0 5 6 12 6 12s6-7 6-12a6 6 0 0 0-6-6z" fill="none" stroke="#fff" stroke-width="1.6"/><circle cx="8" cy="7" r="2" fill="#fff"/></svg><span>14 Alder Ridge Road, Pine Hollow,<br>8120, Larkfield</span></div>
    <div class="row"><svg width="16" height="16" viewBox="0 0 24 24"><path fill="none" stroke="#fff" stroke-width="2" d="M6.6 10.8a15.1 15.1 0 0 0 6.6 6.6l2.2-2.2c.3-.3.7-.4 1-.2 1.1.4 2.3.6 3.6.6.6 0 1 .4 1 1V20c0 .6-.4 1-1 1A17 17 0 0 1 3 4c0-.6.4-1 1-1h3.5c.6 0 1 .4 1 1 0 1.3.2 2.5.6 3.6.1.3 0 .7-.2 1z"/></svg><span>Phone : +0225550192</span></div>
    <div class="row"><svg width="16" height="14" viewBox="0 0 16 14"><rect x="1" y="1" width="14" height="12" fill="none" stroke="#fff" stroke-width="1.6"/><path d="M1 1l7 6 7-6" fill="none" stroke="#fff" stroke-width="1.6"/></svg><span>info@corvantclinicians.example</span></div>
    <div class="social"><span></span><span></span><span></span><span></span></div>
  </div>
  <div class="fcol store">
    <h4>Meridell Wellness Store</h4>
    <ul><li>Meridell Herbal Restoratives</li><li>Nutrition &amp; Nutrient Therapy</li><li>Herbal Apothecary</li><li>Vitamins, Minerals and Supplements</li><li>Forest, Ski, Surf , Golf, Equine Therapy</li><li>Luxury Health Retreats</li></ul>
  </div>
  <div class="fcol branches">
    <h4>Branches</h4>
    <ul><li>Vail</li><li>California</li><li>Hawai</li><li>Aspen</li></ul>
  </div>
  <div class="fcol consult">
    <h4>Online Consultation</h4>
    <div class="in">Enter Name</div>
    <div class="in">Enter Phone</div>
    <div class="in">Enter Email<b>Sign up</b></div>
  </div>
</footer>
<div class="bottom">Copyright 2016 | All Rights Reserved — Meridell Herbal</div>

</body>
</html>
```